Designer Furniture: Brochure Design | Price List | Price Cards

1. brochure 2. price list 3. showroom price cards

We need a brochure design of our high-end wood and acrylic furniture line. We are a custom plastics & acrylics manufacturing company - one facet of our business is custom high-end furniture. We have developed our own proprietary designer furniture line and need a brochure and supporting price list and showroom price cards to reflect the furniture's unique wood and acrylic high-end design appeal.

****More supporting informational & graphic files at:****
https://www.filenook.example/sh/qpwerm7vtbkx3aa/RtyuPlMnBv

We would like to see the following design style: European, modern, clean lines | Lots of white | warm greys | minimalistic in "graphic design" to show off our "furniture design" as the primary focus of the brochure "less is more" | we work in the high-end design market so our look and feel has to reflect that of 'design' | a screenshot of an example of what we like is included in supplied files | we like modern artwork

This is a North American print distribution. Further detailed instructions & details are supplied in the supporting uploaded files of the project.

The winning design may lead to future exclusive design work in this particular facet of our business - possibly others.

* Price list: should be editable PDF (printed on in-house monochrome laser) that is a secondary insert in to the brochure - B&W 6.75"x8.25" Portrait. Includes each item in table or catalogue-type format with dimensions and pricing "$###.##"

* Showroom price card: editable PDF file for each piece of furniture. 5"x7" Portrait OR Landscape. Should include the main 2D dimensional line drawing of each piece along with dimensions and Brookvale Logo or Icon and QRCode from OLD brochure design.
Updates

*****Supporting files & graphic files at:******

- It is imperative that all 3D renderings from our "Rendering" folder in dropbox link be shown in our brochure.

- The price list is a monochrome listing of all our pieces of furniture with dimensions and prices in a table or catalogue-type format.

Here's to clear up some of the questions you've been asking:

PRICE CARDS:
5"x7" portrait
These cards will be but in to an acrylic stand and sit on each piece of furniture - so would probably be best to design a front and back.
Side #1 with specifics: Product name, product number, dimensions, line drawing, price, Brookvale Logo, QR Code, Contact info
Side #2 the other showcasing 3D image, Product Name, Brookvale logo

PRICE SHEET INSERT:
This is an insert for the brochure cataloguing each of the products, 2D dimensional line drawing, dimensions, product name, product number, price - editable PDF so we can easily change prices and print on our in-house monochrome (black & white) printer. 1 or 2 sided - doesn't matter.  Will fit inside the brochure, so cannot be any larger than 7x8.5 - I would suggest to make .25" smaller than brochure folded size - 6.75x8.25

Target Market(s)

Designers, Architects and High-end Retail Furniture Outlets

Industry/Entity Type

Business

Requirements
Must have
• - Brochure finished folded size must be: 7”w x 8.5”h (PORTRAIT)
- raw print stock is 12.5”x19” – maximum print area is 12”x18.5”
- as long as finished folded size is exactly 7”x8.5” portrait - folding style is up to designer (bifold, 3-panel roll, 4-panel roll)
- Will be digitally printed - RGB on 80lb gloss text
- 3D Render image of each product in the furniture line must be included...see below

****More supporting files & graphic files at:****
Nice to have
• ****Supporting files & graphic files at:****

```html
<!DOCTYPE html>
<html lang="en">
<head>
<meta charset="utf-8">
<title>Brookvale Brochure – Folded Side 2</title>
<link href="https://fonts.googleapis.com/css2?family=PT+Sans+Narrow&family=Didact+Gothic&family=Source+Sans+3:wght@400&display=swap" rel="stylesheet">
<style>
  :root {
    --page: #ffffff;
    --frame: #c9c6c3;
    --rule: #bdb9b5;
    --heading: #5b4c42;
    --ink: #1d1a18;
    --caption: #2a2a2a;
    --thumb-border: #b9b5ae;
  }
  * { margin: 0; padding: 0; box-sizing: border-box; }
  html, body { width: 1200px; height: 1000px; overflow: hidden; background: var(--page); }
  .canvas { position: relative; width: 1200px; height: 1000px; }

  .spread {
    position: absolute; left: 203px; top: 222px; width: 813px; height: 494px;
    border: 1px solid var(--frame);
  }
  .fold { position: absolute; left: 405px; top: 0; width: 1px; height: 100%; background: var(--frame); }

  .panel-title {
    position: absolute; font-family: "PT Sans Narrow", sans-serif; font-size: 14px; font-weight: 400;
    color: var(--heading); letter-spacing: 0.1px; line-height: 1;
  }
  .title-rule { position: absolute; border-top: 1px solid var(--rule); border-right: 1px solid var(--rule); }

  .body-copy {
    position: absolute; font-family: "Didact Gothic", sans-serif; font-size: 9.9px;
    line-height: 10.6px; letter-spacing: 0.05px; color: var(--ink);
    text-align: justify; hyphens: manual; -webkit-hyphens: manual;
  }
  .body-copy p + p { margin-top: 10.6px; }
  .drop-cap {
    float: left; font-family: "PT Sans Narrow", sans-serif; font-size: 30px; line-height: 22px;
    margin: -1px 1px 0 0; color: var(--ink);
  }

  .photo { position: absolute; }
  .photo.forest {
    background:
      radial-gradient(circle at 25% 30%, #b0683f 0%, transparent 30%),
      radial-gradient(circle at 70% 65%, #c07a4e 0%, transparent 28%),
      radial-gradient(circle at 55% 25%, #7f8a45 0%, transparent 25%),
      linear-gradient(135deg, #4a3a2c 0%, #5f6a3a 45%, #8a5a3c 70%, #3e4a2c 100%);
  }
  .photo.logs {
    background:
      radial-gradient(ellipse 58% 62% at 48% 52%, #c6a07e 0%, #b38c6a 55%, #6e6a68 80%, transparent 82%),
      linear-gradient(160deg, #8a7868 0%, #5e5550 50%, #8d7a6a 100%);
  }

  .render { position: absolute; border: 1px solid var(--thumb-border); }
  .render.bench {
    background:
      radial-gradient(ellipse 45% 18% at 48% 30%, #a8906e 0%, rgba(168,144,110,0.25) 60%, transparent 100%),
      linear-gradient(180deg, #fbfaf8 0%, #ece8e1 100%);
  }
  .render.lamp {
    background:
      radial-gradient(ellipse 35% 10% at 48% 27%, #ffffff 0%, transparent 100%),
      radial-gradient(ellipse 32% 34% at 48% 70%, #8f806a 0%, rgba(143,128,106,0.3) 70%, transparent 100%),
      linear-gradient(180deg, #e9e9e8 0%, #c9c8c6 100%);
  }
  .render.side-table {
    background:
      radial-gradient(ellipse 26% 32% at 50% 58%, #8c7a5e 0%, rgba(140,122,94,0.25) 70%, transparent 100%),
      linear-gradient(180deg, #fbfbf9 0%, #eeece6 100%);
  }
  .render.coffee-table {
    background:
      radial-gradient(ellipse 40% 16% at 48% 35%, #9a7d58 0%, rgba(154,125,88,0.25) 65%, transparent 100%),
      linear-gradient(180deg, #f4f1ea 0%, #e4dfd2 100%);
  }

  .fold-label {
    position: absolute; left: 0; width: 1200px; top: 756px; text-align: center;
    font-family: "Source Sans 3", sans-serif; font-size: 19px; color: var(--caption);
  }
</style>
</head>
<body>
<div class="canvas">
  <section class="spread">
    <div class="fold"></div>

    <h2 class="panel-title" style="left:14px; top:20px;">Brookvale Brochure Copy</h2>
    <div class="title-rule" style="left:144px; top:29px; width:52px; height:264px;"></div>

    <div class="body-copy" style="left:14px; top:289px; width:181px;">
      <p><span class="drop-cap">T</span>he Brookvale Collection celebrates the complexities of nature by juxtaposing the non-linear “blue-stain” ribbon that permeates each unique piece of wood with the clean lines and transparency of the synthetic-based Clarite.</p>
      <p>Each piece of this line carries clean, rectangular lines and edges. Each remains faithful to the urban design appeal yet showcases the natural warmth and softness of the wood hovering in the face of gravity.</p>
      <p style="text-align:left;">The Brookvale collection is a tribute to the</p>
    </div>

    <div class="photo forest" role="img" aria-label="Aerial view of a pine forest with beetle-killed trees in rust and green tones" style="left:209px; top:14px; width:182px; height:131px;"></div>
    <div class="photo logs" role="img" aria-label="Cut end of a blue-stained lodgepole pine log in a stack" style="left:209px; top:159px; width:182px; height:131px;"></div>

    <div class="body-copy" style="left:209px; top:300px; width:182px;">
      <p>800 million cubic metres of Lodgepole Pine that have been killed by the Moun&shy;tain Pine Beetle (MPB) in the Interior of British Columbia.</p>
      <p>The pieces are named using words from Chinook Jargon. Chinook Jargon was the unifying trade language of the Pacific Northwest during the 19th century. It was the working language in many of the towns and communities in British Columbia that have been most impact&shy;ed by the devastation of the Mountain Pine Beetle.</p>
    </div>

    <h2 class="panel-title" style="left:421px; top:20px;">Organic Modern</h2>
    <div class="title-rule" style="left:505px; top:29px; width:45px; height:451px;"></div>

    <div class="render bench" role="img" aria-label="3D render of a blue-stain wood bench on clear acrylic legs" style="left:563px; top:14px; width:234px; height:130px;"></div>
    <div class="render lamp" role="img" aria-label="3D render of a wood block lamp with a glowing acrylic top" style="left:563px; top:158px; width:111px; height:176px;"></div>
    <div class="render side-table" role="img" aria-label="3D render of a V-shaped wood side table with an acrylic top" style="left:687px; top:158px; width:110px; height:113px;"></div>
    <div class="render coffee-table" role="img" aria-label="3D render of a coffee table with a wood beam and clear acrylic top and legs" style="left:563px; top:348px; width:234px; height:131px;"></div>
  </section>

  <p class="fold-label">Folded side 2</p>
</div>
</body>
</html>
```